Morvane Estates Business Card and Email Signature Design

I am a Brokiva and need a business card design with my head shot picture and logo and contact information that can be prepared to be used on my email signature as well. I would like my head shot image background to match the background of the business card. So in other words the background of my head shot should be transparent. I would like the Brokiva Logo on there and also MLS and Civic Nestmark Logo. My email address is: lina@morvaneestates.example, Phone Number is: 555-614-7290, website: www.morvaneestates.example Address: 20874 Quillfeather Court Fenwick, OR 47518
I also need just the head shot photo with white background in a JPEG file as well so I can upload that picture to my ProfLoop and Hausora profiles.

```html
<!DOCTYPE html>
<html lang="en">
<head>
<meta charset="utf-8">
<title>Morvane Estates – Business Card</title>
<link href="https://fonts.googleapis.com/css2?family=Bebas+Neue&family=Roboto:wght@300;400;700&display=swap" rel="stylesheet">
<style>
  :root {
    --stage: #1c1d1f;
    --card-white: #ffffff;
    --brand-blue: #17577c;
    --brand-blue-deep: #0f4262;
    --ink-blue: #1b5a86;
    --ink-grey: #555a60;
    --ghost: #f1f2f3;
    --photo-top: #5a5e66;
    --photo-bottom: #2f3238;
  }
  * { box-sizing: border-box; margin: 0; padding: 0; }
  html, body {
    width: 1200px; height: 963px; overflow: hidden;
    background: var(--stage);
    font-family: "Roboto", sans-serif;
  }
  .sheet { position: relative; width: 1200px; height: 963px; }
  .card {
    position: absolute; left: 250px; width: 700px; height: 400px;
    border-radius: 16px; overflow: hidden;
  }
  .card--front { top: 60px; background: var(--card-white); }
  .card--back {
    top: 503px;
    background: linear-gradient(160deg, var(--brand-blue) 0%, var(--brand-blue-deep) 100%);
  }

  /* front */
  .front__ghost {
    position: absolute; left: 250px; top: 60px;
    width: 300px; height: 300px; border-radius: 50%;
    background: var(--ghost);
  }
  .front__identity {
    position: absolute; left: 20px; top: 150px; width: 305px; text-align: right;
    white-space: nowrap;
  }
  .front__name {
    font-family: "Bebas Neue", sans-serif;
    font-size: 48px; letter-spacing: 2px; line-height: 1;
    color: var(--ink-blue);
  }
  .front__title {
    font-size: 15px; font-weight: 300; color: var(--ink-grey); margin-top: 4px;
  }
  .front__rule {
    position: absolute; left: 342px; top: 130px;
    width: 3px; height: 140px; background: var(--ink-blue);
  }
  .front__contact {
    position: absolute; left: 372px; top: 130px;
    list-style: none; font-size: 15px; font-weight: 300; color: var(--ink-grey);
    line-height: 1.55; white-space: nowrap;
  }
  .front__contact li { display: flex; align-items: center; gap: 8px; }
  .front__contact svg { width: 12px; height: 12px; fill: var(--ink-blue); flex: none; }

  /* back */
  .back__headshot {
    position: absolute; left: 0; bottom: 0; width: 290px; height: 380px;
    background: linear-gradient(180deg, var(--photo-top), var(--photo-bottom));
    border-top-right-radius: 140px 120px;
  }
  .back__brand {
    position: absolute; left: 300px; top: 110px; width: 390px; text-align: center;
    color: var(--card-white); white-space: nowrap;
  }
  .back__mark {
    width: 96px; height: 96px; border-radius: 50%;
    background: var(--card-white); margin: 0 auto 18px;
  }
  .back__name {
    font-size: 32px; font-weight: 700; letter-spacing: 1px; text-transform: uppercase;
    line-height: 1.1;
  }
  .back__tagline {
    font-size: 15px; font-weight: 400; letter-spacing: 4px; text-transform: uppercase;
    margin-top: 6px;
  }
</style>
</head>
<body>
<main class="sheet">

  <section class="card card--front" aria-label="Business card front">
    <div class="front__ghost"></div>
    <div class="front__identity">
      <h1 class="front__name">Lina Corvell</h1>
      <p class="front__title">Brokiva</p>
    </div>
    <div class="front__rule"></div>
    <ul class="front__contact">
      <li>20874 Quillfeather Court</li>
      <li>Fenwick, OR 47518</li>
      <li>
        <svg viewBox="0 0 24 24" aria-hidden="true"><path d="M6.6 10.8a15 15 0 0 0 6.6 6.6l2.2-2.2c.3-.3.7-.4 1-.2 1.1.4 2.3.6 3.6.6.6 0 1 .4 1 1V20c0 .6-.4 1-1 1A17 17 0 0 1 3 4c0-.6.4-1 1-1h3.5c.6 0 1 .4 1 1 0 1.3.2 2.5.6 3.6.1.3 0 .7-.2 1z"/></svg>
        555-614-7290
      </li>
      <li>
        <svg viewBox="0 0 24 24" aria-hidden="true"><path d="M2 5h20v14H2zm2 2v.5l8 5 8-5V7zm0 2.8V17h16V9.8l-8 5z"/></svg>
        lina@morvaneestates.example
      </li>
      <li>
        <svg viewBox="0 0 24 24" aria-hidden="true"><path d="M12 2a10 10 0 1 0 0 20 10 10 0 0 0 0-20zm6.9 9h-3a15 15 0 0 0-1.3-5.6A8 8 0 0 1 18.9 11zM12 4.1c.9 1.2 1.7 3.6 1.9 6.9h-3.8c.2-3.3 1-5.7 1.9-6.9zM9.4 5.4A15 15 0 0 0 8.1 11h-3a8 8 0 0 1 4.3-5.6zM5.1 13h3a15 15 0 0 0 1.3 5.6A8 8 0 0 1 5.1 13zM12 19.9c-.9-1.2-1.7-3.6-1.9-6.9h3.8c-.2 3.3-1 5.7-1.9 6.9zm2.6-1.3a15 15 0 0 0 1.3-5.6h3a8 8 0 0 1-4.3 5.6z"/></svg>
        www.morvaneestates.example
      </li>
    </ul>
  </section>

  <section class="card card--back" aria-label="Business card back">
    <div class="back__headshot" role="img" aria-label="Head shot of the agent in a dark suit and striped tie, background removed"></div>
    <div class="back__brand">
      <div class="back__mark"></div>
      <p class="back__name">Morvane Estates</p>
      <p class="back__tagline">Real Estate Services</p>
    </div>
  </section>

</main>
</body>
</html>
```